Verpackungsdesign für Parfüm gesucht
Zielgruppe
Wir werden eine Marke unter dem Namen ORMAL mit Parfüm auf dem Markt bringen und benötigen hierfür ein hochwertiges Design . Unsre Zielgruppe ist m/w/d und zwischen 16 und 60 Jahre.
Aufgabenstellung
Bei der Verpackung handelt es sich um eine Schiebeschachtel. Wir benötigen das Design nur für die Außenhülle, nicht für den Schuber.
Pflichtangaben auf der Verpackung sind unser Logo, Eau de Parfum, High Intense, 20 ml e 0.67 FL OZ,
Natural Spray Vaporisateur,

```html
<!DOCTYPE html>
<html lang="en">
<head>
<meta charset="utf-8">
<title>ORMAL – Eau de Parfum Sleeve</title>
<link rel="stylesheet" href="https://fonts.googleapis.com/css2?family=EB+Garamond:wght@400;500&display=swap">
<style>
  :root {
    --backdrop: #b9b8b9;
    --sleeve-dark: #221f1e;
    --sleeve-mid: #2e2b29;
    --sleeve-light: #4d4946;
    --ink-light: #d6d6d6;
    --ink-side: #c9c9c9;
    --label-fill: #dcdcdc;
    --label-ink: #2a2725;
  }
  * { margin: 0; padding: 0; box-sizing: border-box; }
  html, body {
    width: 1200px; height: 960px; overflow: hidden;
    background: var(--backdrop);
  }
  .sleeve-net {
    position: absolute;
    left: 330px; top: 80px;
    display: flex;
    height: 800px;
  }
  .side-panel {
    position: relative;
    width: 140px; height: 100%;
    background: var(--sleeve-dark);
    overflow: hidden;
    border-right: 1px solid #151312;
  }
  .side-wordmark {
    position: absolute;
    left: 50%; top: 50%;
    transform: translate(-50%, -50%) rotate(-90deg);
    font-family: "EB Garamond", serif;
    font-weight: 400;
    font-size: 218px;
    line-height: 1;
    letter-spacing: 6px;
    color: var(--ink-side);
    white-space: nowrap;
  }
  .front-panel {
    position: relative;
    width: 400px; height: 100%;
    background: linear-gradient(90deg, var(--sleeve-dark) 0%, var(--sleeve-mid) 45%, var(--sleeve-light) 100%);
    font-family: "EB Garamond", serif;
    color: var(--ink-light);
  }
  .brand-name {
    position: absolute;
    left: 46px; top: 92px;
    font-size: 72px;
    font-weight: 400;
    letter-spacing: 4px;
    line-height: 1;
  }
  .spray-note {
    position: absolute;
    left: 46px; top: 222px;
    font-size: 27px;
    line-height: 1.55;
  }
  .intensity-label {
    position: absolute;
    right: 0; top: 470px;
    width: 178px; height: 92px;
    background: var(--label-fill);
    color: var(--label-ink);
    font-size: 29px;
    font-weight: 500;
    display: flex; align-items: center; justify-content: center;
  }
  .product-footer {
    position: absolute;
    left: 46px; right: 40px; top: 640px;
    border-top: 2px solid var(--ink-light);
  }
  .product-type {
    display: flex; justify-content: space-between; align-items: baseline;
    padding: 8px 0 6px;
    border-bottom: 2px solid var(--ink-light);
  }
  .product-type .name { font-size: 37px; font-weight: 500; }
  .product-type .volume-ml { font-size: 26px; }
  .volume-oz {
    margin-top: 8px;
    font-size: 29px;
  }
</style>
</head>
<body>
  <div class="sleeve-net">
    <div class="side-panel">
      <span class="side-wordmark">ORMAL</span>
    </div>
    <div class="front-panel">
      <div class="brand-name">ORMAL</div>
      <div class="spray-note">Natural Spray<br>Vaporisateur</div>
      <div class="intensity-label">High Intense</div>
      <div class="product-footer">
        <div class="product-type">
          <span class="name">Eau de Parfum</span>
          <span class="volume-ml">20ml</span>
        </div>
        <div class="volume-oz">0.67 FL OZ</div>
      </div>
    </div>
  </div>
</body>
</html>
```